web design needed for brivolent safety ltd

We need a web design for our new company. It is called Brivo Lent Safety Ltd and is a company based around a security/safety/info box specifically made for on construction sites, but could be used elsewhere. It is completely portable with a builtin alarm system with remote. There is a larger box and a smaller box (only have an image for this one at this stage, I will get better photos of the temp box soon, but this one will make a start).
This will be the standard box that is for sale, howver you can get upgrades that include a fire extinguisher, first aid kit, hand sanitizer, fire blanket.
Other features include a place for plans and safety info for the site, a hook attached to the back of the smaller box so it can be hung on the door. Both boxes are suitable for outside.
We would like the wesite to incorporate our logo and pictures of the box. I have attached our logo and an exaple of a mock box as the final box is still being made sothese photos will be swapped once we have it from the manufacturer.
We would like the following pages:
Home (possibly a picture of the box rotating, doesnt have to though?)
About us
Products
FAQ
Shopping cart
Contact us
We would like the style to be crisp, simple and not to busy.
Thanks
Updates
More photos of the box have been added. These are for the larger box.
Reason: we are happy to give people more time so have extended it by seven days
Target Market(s)
Builders mainly
Industry/Entity Type
Construction
Font styles to use
Other font styles liked:
- ERAS BOLD ITC
Look and feel
Each slider illustrates characteristics of the customer's brand and the style your logo design should communicate.

```html
<!DOCTYPE html>
<html lang="en">
<head>
<meta charset="utf-8">
<title>Brivolent Safety – Protect Your Family</title>
<link rel="stylesheet" href="https://fonts.googleapis.com/css2?family=Lato:wght@400;700;900&display=swap">
<style>
:root{
  --ink:#222;
  --dark:#1d2023;
  --dark-2:#25292d;
  --green:#8cc63f;
  --blue:#2ba3d6;
  --blue-btn:#2d8fd8;
  --grey-band:#e4e4e4;
  --muted:#777;
  --line:#e3e3e3;
  --white:#fff;
}
*{margin:0;padding:0;box-sizing:border-box}
html,body{width:1200px;height:2687px;overflow:hidden}
body{font-family:"Lato",Arial,sans-serif;color:var(--ink);background:var(--white);position:relative}
.abs{position:absolute}

/* header */
.site-header{position:absolute;left:0;top:0;width:1200px;height:90px;background:var(--dark)}
.brand{position:absolute;left:150px;top:22px;display:flex;align-items:center;gap:14px}
.brand-mark{width:42px;height:42px;background:var(--green);border-radius:4px}
.brand-name{font-weight:900;font-size:25px;color:var(--white);letter-spacing:.5px}
.cart{position:absolute;right:155px;top:12px;font-size:12px;color:var(--green);display:flex;align-items:center;gap:8px}
.main-nav{position:absolute;right:148px;top:44px;display:flex;gap:26px}
.main-nav a{color:var(--white);text-decoration:none;font-weight:700;font-size:16px}

/* hero */
.hero-photo{left:0;top:90px;width:1200px;height:560px;background:radial-gradient(ellipse at 20% 10%,#fbf6c8 0%,#d9e27a 30%,#b9c456 55%,#8f9a3e 100%)}
.hero-title{left:148px;top:236px;font-weight:900;font-size:40px;color:#111;letter-spacing:.3px}
.hero-text{left:150px;top:288px;width:440px;font-size:13.5px;line-height:19px;color:#111}
.kit-photo{background:linear-gradient(160deg,#ff5a3c,#d8261a);border-radius:18px}
.kit-hero{left:146px;top:493px;width:302px;height:235px}
.offer-band{left:0;top:650px;width:1200px;height:89px;background:var(--grey-band)}
.offer-text{left:477px;top:668px;width:360px;font-size:13px;line-height:19px;color:#333}
.btn{display:flex;align-items:center;justify-content:center;color:var(--white);text-decoration:none;border-radius:3px}
.btn-hero{left:900px;top:672px;width:139px;height:36px;background:var(--blue-btn);font-size:13px}

/* products */
.section-title{left:0;width:1200px;text-align:center;font-weight:900;font-size:28px;top:781px;color:#333}
.section-lede{left:320px;width:560px;top:833px;text-align:center;font-size:13px;line-height:18px;color:var(--muted)}
.kit-large{left:313px;top:940px;width:202px;height:157px}
.kit-small{left:712px;top:963px;width:166px;height:134px}
.price-card{position:absolute;top:1124px;width:206px;border:1px solid var(--line);background:var(--white);text-align:center}
.price-card.standard{left:311px}
.price-card.small{left:692px}
.card-head{background:var(--blue);color:var(--white);font-weight:700;font-size:16px;height:36px;line-height:36px}
.card-price{height:36px;line-height:36px;font-size:17px;border-bottom:1px solid var(--line);background:#f6f6f6}
.card-features{list-style:none}
.card-features li{height:37px;line-height:37px;font-size:12px;color:#8a8a8a;border-bottom:1px solid var(--line);margin:0 12px}
.card-features li:last-child{border-bottom:none}
.card-btn{margin:10px 9px 14px;height:28px;background:var(--blue);font-size:12px}

/* video */
.video-band{left:0;top:1610px;width:1200px;height:475px;background:linear-gradient(180deg,#7a8a92 0%,#6d705e 45%,#4a4b3c 100%)}
.video-frame{left:157px;top:1708px;width:436px;height:273px;background:linear-gradient(180deg,#c9d7df 0%,#b4b49a 55%,#8a8470 100%)}
.video-bar{position:absolute;left:8px;bottom:8px;right:8px;height:34px;background:rgba(20,20,20,.85);display:flex;align-items:center;gap:12px;padding:0 10px}
.play{width:40px;height:26px;background:#111;border-radius:3px;display:flex;align-items:center;justify-content:center}
.track{flex:1;height:6px;background:#555;border-radius:3px;position:relative}
.track::before{content:"";position:absolute;left:0;top:0;height:6px;width:12%;background:var(--green);border-radius:3px}
.vtime{color:#ddd;font-size:10px}
.video-title{left:616px;top:1712px;width:420px;color:var(--white);font-weight:900;font-size:28px;line-height:34px}
.video-title span{font-weight:700;font-size:26px}
.video-text{left:616px;top:1816px;width:400px;color:var(--white);font-size:12px;line-height:18px}

/* testimonial */
.testimonial-band{left:0;top:2085px;width:1200px;height:423px;background:linear-gradient(135deg,#d8d8d8,#bdbdbd 50%,#d2d2d2)}
.quote-box{left:157px;top:2167px;width:871px;height:233px;background:#000;color:var(--white);text-align:center}
.quote{position:absolute;left:70px;right:70px;top:42px;font-style:italic;font-size:13px;line-height:22px}
.qmark{position:absolute;color:var(--blue);font-size:46px;font-weight:900;line-height:1}
.q-open{left:40px;top:34px}.q-close{left:628px;top:108px}
.author{position:absolute;left:0;right:0;top:149px;font-size:14px}
.role{position:absolute;left:0;right:0;top:175px;font-size:12px;color:#bbb}

/* footer */
.site-footer{left:0;top:2508px;width:1200px;height:179px;background:var(--dark-2);text-align:center;color:#9a9a9a}
.foot-nav{position:absolute;top:20px;left:0;right:0;font-size:13px}
.foot-nav a{color:#aaa;text-decoration:none}
.foot-legal{position:absolute;top:44px;left:0;right:0;font-size:10px}
.pay{position:absolute;top:69px;left:497px;display:flex;gap:11px}
.pay span{width:46px;height:31px;border-radius:3px;background:#f1f1f1}
.pay span:nth-child(1){background:#e9edf5}
.pay span:nth-child(3){background:#cfe3f3}
.pay span:nth-child(4){background:#f4e39a}
.copy{position:absolute;top:120px;left:0;right:0;font-size:10px;color:#777}
</style>
</head>
<body>

<header class="site-header">
  <div class="brand"><span class="brand-mark"></span><span class="brand-name">BRIVOLENT SAFETY</span></div>
  <div class="cart">
    <svg width="18" height="14" viewBox="0 0 18 14"><path d="M0 1h3l2 8h10l2-6H4.5" fill="none" stroke="#8cc63f" stroke-width="1.6"/><circle cx="6.5" cy="12" r="1.4" fill="#8cc63f"/><circle cx="13.5" cy="12" r="1.4" fill="#8cc63f"/></svg>
    Cart | 0 | item
  </div>
  <nav class="main-nav"><a href="#">Home</a><a href="#">About us</a><a href="#">Products</a><a href="#">FAQ</a><a href="#">Contact us</a></nav>
</header>

<div class="abs hero-photo" role="img" aria-label="Mother holding a smiling baby on a sunny meadow"></div>
<h1 class="abs hero-title">PROTECT YOUR FAMILY</h1>
<p class="abs hero-text">Lorem ipsum dolor sit amet, consectetuer adipiscing elit. Aenean commodo ligula eget dolor. Aenean massa. Cum sociis natoque penatibus et magnis dis parturient montes, nascetur ridiculus mus. Donec quam felis, ultricies nec, pellentesque eu, pretium quis, sem.</p>
<div class="abs offer-band"></div>
<div class="abs kit-photo kit-hero" role="img" aria-label="Red emergency first aid kit bag"></div>
<p class="abs offer-text">With or Product Medic Kit lorem ipsum dolor sit amet, consectetuer adipiscing elit. Aenean commodo ligula .</p>
<a class="abs btn btn-hero" href="#">PURCHASE NOW</a>

<h2 class="abs section-title">IT'S TIME TO PROTECT YOUR FAMILY</h2>
<p class="abs section-lede">Lorem ipsum dolor sit amet, consectetuer adipiscing elit. Aenean commodo ligula eget dolor. Aenean massa. Cum sociis natoque penatibus et magnis dis parturient montes, nascetur ridiculus mus.</p>

<div class="abs kit-photo kit-large" role="img" aria-label="Standard safety box, red kit bag"></div>
<div class="abs kit-photo kit-small" role="img" aria-label="Small safety box, red kit bag"></div>

<div class="price-card standard">
  <div class="card-head">STANDART BOX</div>
  <div class="card-price">$244.00</div>
  <ul class="card-features">
    <li>Fire Extinguisher</li><li>First Aid Kit</li><li>Hand Sanitizer</li><li>Fire Blanket</li>
    <li>Another</li><li>Another</li><li>Place for Plans</li><li>Additional Feature</li>
  </ul>
  <a class="btn card-btn" href="#">Purchase Now</a>
</div>

<div class="price-card small">
  <div class="card-head">SMALLBOX</div>
  <div class="card-price">$199.00</div>
  <ul class="card-features">
    <li>Fire Extinguisher</li><li>First Aid Kit</li><li>Hand Sanitizer</li><li>Fire Blanket</li>
    <li>Another</li><li>Another</li>
  </ul>
  <a class="btn card-btn" href="#">Purchase Now</a>
</div>

<div class="abs video-band" role="img" aria-label="Family relaxing together in a garden chair outdoors"></div>
<div class="abs video-frame" role="img" aria-label="Video still of a family sitting outside with their dog">
  <div class="video-bar">
    <div class="play"><svg width="12" height="14" viewBox="0 0 12 14"><path d="M1 1l10 6-10 6z" fill="#fff"/></svg></div>
    <span class="vtime">00:04</span>
    <div class="track"></div>
    <span class="vtime">HD</span>
  </div>
</div>
<h3 class="abs video-title">Lorem ipsum dolor sit<br><span>amet, consectetuer adipiscing</span></h3>
<p class="abs video-text">Aenean commodo ligula eget dolor. Aenean massa. Cum sociis natoque penatibus et magnis dis parturient montes, nascetur ridiculus mus. Donec quam felis, ultricies nec, pellentesque eu, pretium quis, sem. Nulla consequat massa quis enim. Donec pede justo, fringilla vel, aliquet nec, vulputate eget, arcu. In enim justo, rhoncus ut, imperdiet a, venenatis vitae, justo. Nullam dictum felis eu pede mollis pretium. Integer tincidunt.</p>

<div class="abs testimonial-band" role="img" aria-label="Grey mosaic of customer portrait photos"></div>
<div class="abs quote-box">
  <span class="qmark q-open">&ldquo;</span>
  <p class="quote">Lorem ipsum dolor sit amet, consectetuer adipiscing elit. Aenean commodo ligula eget dolor. Aenean massa. Cum sociis natoque penatibus et magnis dis parturient montes, nascetur ridiculus mus. Donec quam felis, ultricies nec, pellentesque eu, pretium quis, sem. Nulla consequat massa quis enim. Donec pede justo, fringilla vel, aliquet nec, vulputate eget, arcu. In enim justo</p>
  <span class="qmark q-close">&rdquo;</span>
  <p class="author">- Maren Tolle</p>
  <p class="role">Designer- Norvel Works</p>
</div>

<footer class="abs site-footer">
  <nav class="foot-nav"><a href="#">Home</a> | <a href="#">About us</a> | <a href="#">Products</a> | <a href="#">FAQ</a> | <a href="#">Shopping cart</a> | <a href="#">Contact us</a></nav>
  <p class="foot-legal">Privacy Policy | Terms of Service</p>
  <div class="pay"><span></span><span></span><span></span><span></span></div>
  <p class="copy">© Copyright 2013 All Rights Reserved.</p>
</footer>

</body>
</html>
```